Direct to Consumer extended service contract business with a new disruptive business model needs a

We need a customized wordpress design for a company called 'Tall Harbor Assurance'.
We provide an innovative and unique service contract protection program direct to consumers. This program provides monthly coverage for all electronics purchased in the last 4 years and all electronics the consumer purchases in the future for a low monthly fee. The overall design should communicate a sense of legitimacy, ethics, and superior customer service and support (in an industry that has a huge PR issue to overcome).
Electronics is the first product group, other product groups with different price points to launch in the future..

Target Market(s)

All purchasers of electronic goods...all demographics

Industry/Entity Type

Electronics

Font styles to use
Sans Serif

Requirements
Must have
• Customer Testimonials
Industry News
Customer ratings
Blog posts
Call to action messaging
Like the functional elements and design of bramblequill.example (need to be better)
Nice to have
• Like to see video testimonials
Social network "whats trending related to electronics or service contract industry"
Easy way to register products for warranty

```html
<!DOCTYPE html>
<html lang="en">
<head>
<meta charset="utf-8">
<title>Tall Harbor Assurance</title>
<link href="https://fonts.googleapis.com/css2?family=Lato:wght@400;700;900&display=swap" rel="stylesheet">
<style>
:root{
  --green:#2e9e44;
  --green-light:#38ad4d;
  --green-dark:#1f7a33;
  --green-bright:#3fe05a;
  --green-text:#1f8a38;
  --ink:#2b2b2b;
  --band:#333333;
  --head-bg:#e9e9e9;
  --white:#ffffff;
  --grey-text:#444;
}
*{margin:0;padding:0;box-sizing:border-box}
html,body{width:798px;height:1200px;overflow:hidden;background:var(--white)}
body{font-family:'Lato',sans-serif;color:var(--ink);position:relative}
.abs{position:absolute}
.site-header{left:0;top:0;width:798px;height:70px;background:var(--head-bg)}
.brand{left:93px;top:20px;font-weight:900;font-size:22px;color:var(--green-text);letter-spacing:1px}
.brand-sub{left:93px;top:46px;font-size:8px;letter-spacing:5px;color:#555}
.call-now{left:541px;top:51px;font-weight:700;font-size:13px;color:var(--green-text)}
.nav{left:0;top:70px;width:798px;height:41px;background:var(--green)}
.nav ul{list-style:none;display:flex;gap:23px;position:absolute;left:90px;top:13px}
.nav li{color:var(--white);font-size:11.5px}
.phone{left:532px;top:70px;width:198px;height:41px;background:var(--green-dark);color:var(--white);font-size:14px;display:flex;align-items:center;justify-content:center}
.hero{left:0;top:111px;width:798px;height:310px;background:linear-gradient(#2f9f44,#2a9340)}
.hero-media{left:100px;top:160px;width:266px;height:230px;border-radius:8px;background:linear-gradient(135deg,#0e1c2c,#7fa6c9 55%,#14283c)}
.arrow{width:32px;height:32px;border-radius:50%;background:rgba(255,255,255,.15);top:252px}
.hero-line{left:409px;color:var(--white);font-size:16.5px}
.hero-line b{color:var(--green-bright);font-weight:700}
.hero-btn{left:406px;top:254px;width:261px;height:29px;background:var(--white);border-radius:3px;color:var(--green-text);font-weight:700;font-size:11px;display:flex;align-items:center;justify-content:center}
.hero-title{left:409px;top:298px;color:var(--white);font-weight:700;font-size:19.5px}
.hero-sub{left:409px;top:327px;color:var(--white);font-weight:700;font-size:11px}
.cta-band{left:0;top:421px;width:798px;height:68px;background:var(--band)}
.cta-text{left:184px;top:446px;color:var(--white);font-weight:700;font-size:15.5px}
.cta-btn{left:515px;top:440px;width:91px;height:30px;background:var(--green);border-radius:4px;color:var(--white);font-weight:700;font-size:16px;display:flex;align-items:center;justify-content:center}
.h2{font-weight:700;font-size:15.5px;color:var(--ink)}
.lead{color:var(--green-text);font-size:11.8px;line-height:14.5px;white-space:nowrap}
.small{font-size:8px;line-height:12px;color:var(--ink);white-space:nowrap}
.btn{background:var(--green-dark);color:var(--white);font-weight:700;font-size:9.5px;border-radius:3px;display:flex;align-items:center;justify-content:center;box-shadow:0 1px 2px rgba(0,0,0,.3)}
.date{width:39px;height:45px;background:var(--green-text);color:var(--white);font-weight:700;font-size:10.5px;line-height:13px;display:flex;align-items:center;justify-content:center;text-align:center}
.news-title{font-size:10.5px;color:var(--grey-text)}
.news-text{font-size:7.5px;line-height:10.5px;color:var(--ink);white-space:nowrap}
.photo{border-radius:2px}
.stars{left:627px;top:746px;color:var(--green-text);font-size:12px;letter-spacing:2px}
.blog-title{font-size:12.5px;color:var(--ink)}
.blog-text{font-size:8.5px;line-height:11.5px;color:var(--ink);white-space:nowrap}
.btn-light{background:var(--green);color:var(--white);font-size:10px;border-radius:3px;display:flex;align-items:center;justify-content:center;box-shadow:0 1px 2px rgba(0,0,0,.3)}
.community-dot{left:390px;top:834px;width:42px;height:42px;border-radius:50%;background:var(--green-dark)}
.join-btn{left:406px;top:997px;width:116px;height:37px;background:var(--green);border-radius:5px;color:var(--white);font-weight:700;font-size:16px;display:flex;align-items:center;justify-content:center;box-shadow:0 2px 3px rgba(0,0,0,.3)}
.footer{left:0;top:1057px;width:798px;height:143px;background:var(--green)}
.f-head{color:var(--white);font-size:15px;top:1071px}
.f-link{color:var(--white);font-size:10px;line-height:16px}
.field{left:310px;width:178px;height:25px;background:var(--white);font-size:8px;color:#444;padding:8px 11px}
.subscribe{left:312px;top:1167px;width:80px;height:23px;background:var(--band);color:var(--white);font-size:12px;border-radius:3px;display:flex;align-items:center;justify-content:center}
.social{top:1097px;width:25px;height:25px;border-radius:4px;background:rgba(255,255,255,.85)}
.copy{left:582px;top:1177px;color:var(--white);font-size:8px}
</style>
</head>
<body>
<header>
  <div class="abs site-header"></div>
  <div class="abs brand">TALL HARBOR</div>
  <div class="abs brand-sub">ASSURANCE</div>
  <div class="abs call-now">CALL NOW</div>
  <nav class="abs nav"><ul><li>HOME</li><li>PLANS</li><li>BENIFITS</li><li>FAQ'S</li><li>ABOUT US</li><li>LOGIN</li><li>SUPPORT</li></ul></nav>
  <div class="abs phone">855-555-0142</div>
</header>

<section>
  <div class="abs hero"></div>
  <div class="abs hero-media" role="img" aria-label="Tablet and phone showing a digital laptop image"></div>
  <div class="abs arrow" style="left:63px"><svg width="32" height="32"><path d="M18 9l-7 7 7 7" stroke="#1f7a33" stroke-width="1.5" fill="none"/></svg></div>
  <div class="abs arrow" style="left:702px"><svg width="32" height="32"><path d="M14 9l7 7-7 7" stroke="#1f7a33" stroke-width="1.5" fill="none"/></svg></div>
  <div class="abs hero-line" style="top:193px">THE DAYS OF <b>BUYING EXPENSIVE</b></div>
  <div class="abs hero-line" style="top:215px">IN - STORE SERVICE PLAN ARE OVER!</div>
  <div class="abs hero-btn">DON'T BUY ANYMORE IN - STORE SERVICE PLAN</div>
  <div class="abs hero-title">TALL HARBOR ASSURANCE</div>
  <div class="abs hero-sub">IS THE SOLUTION</div>
</section>

<section>
  <div class="abs cta-band"></div>
  <div class="abs cta-text">GET YOUR HARBOR ASSURANCE TODAY!</div>
  <div class="abs cta-btn">SIGN UP</div>
</section>

<section>
  <div class="abs h2" style="left:80px;top:500px">ABOUT US</div>
  <div class="abs lead" style="left:80px;top:526px">Duis aute irure dolor in<br>reprehenderit in voluptate velit esse<br>cillum dolore eu .</div>
  <div class="abs small" style="left:80px;top:576px">Nemo enim ipsam voluptatem quia voluptas sit<br>aspernatur aut odit aut fugit, sed quia consequuntur<br>magni dolores eos qui ratione voluptatem sequi<br>nesciunt. Neque porro quisquam est, qui dolorem<br>ipsum quia dolor sit amet, consectetur,</div>
  <div class="abs small" style="left:80px;top:648px">Adipisci velit, sed quia non numquam eius modi<br>tempora incidunt ut labore et dolore magnam<br>aliquam quaerat voluptatem. Ut enim ad minima<br>veniam, quis nostrum exercitationem ullam</div>
  <div class="abs btn" style="left:77px;top:709px;width:72px;height:23px">READ MORE</div>

  <div class="abs h2" style="left:307px;top:500px">INDUSTRY NEWS</div>
  <div class="abs date" style="left:307px;top:528px">08<br>AUG</div>
  <div class="abs news-title" style="left:357px;top:527px">LORIUM IPSUM</div>
  <div class="abs news-text" style="left:358px;top:544px">Mauris nec volutpat erat. In sed<br>sapien dui. Sed eu neque sit amet<br>purus scelerisque lobortis.</div>
  <div class="abs date" style="left:307px;top:595px">08<br>AUG</div>
  <div class="abs news-title" style="left:357px;top:590px">LORIUM IPSUM</div>
  <div class="abs news-text" style="left:358px;top:607px">Mauris nec volutpat erat. In sed<br>sapien dui. Sed eu neque sit amet<br>purus scelerisque lobortis.</div>
  <div class="abs date" style="left:307px;top:663px">08<br>AUG</div>
  <div class="abs news-title" style="left:357px;top:658px">LORIUM IPSUM</div>
  <div class="abs news-text" style="left:358px;top:675px">Mauris nec volutpat erat. In sed<br>sapien dui. Sed eu neque sit amet<br>purus scelerisque lobortis.</div>
  <div class="abs btn" style="left:309px;top:720px;width:72px;height:23px">READ MORE</div>

  <div class="abs h2" style="left:521px;top:500px">TESTIMONIALS</div>
  <div class="abs photo" style="left:521px;top:526px;width:198px;height:120px;background:linear-gradient(135deg,#e8e6e2,#c9b9a4 60%,#d9d3cb)" role="img" aria-label="Video testimonial from a smiling customer"></div>
  <svg class="abs" style="left:608px;top:576px" width="14" height="18"><path d="M1 1l12 8-12 8z" fill="#333" opacity=".75"/></svg>
  <div class="abs h2" style="left:521px;top:660px">CUSTOMER RATINGS</div>
  <div class="abs" style="left:525px;top:694px;font-weight:700;font-size:12px;color:var(--grey-text)">NOOR HALVARD</div>
  <svg class="abs" style="left:681px;top:694px" width="12" height="8"><path d="M5 0L0 4l5 4zM7 0l5 4-5 4z" fill="#1f8a38"/></svg>
  <div class="abs" style="left:525px;top:713px;font-size:9.5px;line-height:12px;color:var(--grey-text);white-space:nowrap">Mauris nec volutpat erat. In sed sapien dui.<br>Sed eu neque sit amet purus scelerisque<br>lobortis.</div>
  <div class="abs stars">★★★★</div>
</section>

<section>
  <div class="abs h2" style="left:90px;top:797px">MY BLOG POSTS</div>
  <div class="abs photo" style="left:90px;top:836px;width:75px;height:70px;background:linear-gradient(135deg,#2f6fa8,#9dc0de 55%,#1c2d44)" role="img" aria-label="Businessman touching a digital interface"></div>
  <div class="abs blog-title" style="left:172px;top:836px">LORIUM IPSUM</div>
  <div class="abs blog-text" style="left:172px;top:856px">Sed ut perspiciatis unde omnis iste natus error sit<br>voluptatem accusantium doloremque laudan-<br>tium, totam rem aperiam, eaque ipsa quae ab illo<br>inventore veritatis</div>
  <div class="abs btn-light" style="left:301px;top:906px;width:63px;height:23px">READ MORE</div>
  <div class="abs photo" style="left:90px;top:936px;width:75px;height:70px;background:linear-gradient(135deg,#e9e6e0,#b8a48d 60%,#7c8a9c)" role="img" aria-label="Woman sitting on the floor using a laptop"></div>
  <div class="abs blog-title" style="left:173px;top:936px">LORIUM IPSUM</div>
  <div class="abs blog-text" style="left:173px;top:956px">Sed ut perspiciatis unde omnis iste natus error sit<br>voluptatem accusantium doloremque laudan-<br>tium, totam rem aperiam, eaque ipsa quae ab illo<br>inventore veritatis</div>
  <div class="abs btn-light" style="left:301px;top:1006px;width:63px;height:23px">READ MORE</div>

  <div class="abs h2" style="left:391px;top:803px">JOIN OUR COMMUNITY</div>
  <div class="abs community-dot"></div>
  <div class="abs" style="left:443px;top:840px;font-size:10px;line-height:13px;white-space:nowrap">Sed ut perspiciatis unde omnis iste natus error sit<br>voluptatem .</div>
  <div class="abs photo" style="left:403px;top:902px;width:67px;height:64px;background:linear-gradient(135deg,#e6d6c4,#b98f6c)" role="img" aria-label="Community member portrait"></div>
  <div class="abs photo" style="left:477px;top:902px;width:67px;height:64px;background:linear-gradient(135deg,#e4e4e4,#b08a6c)" role="img" aria-label="Community member portrait"></div>
  <div class="abs photo" style="left:552px;top:902px;width:67px;height:64px;background:linear-gradient(135deg,#d9d9d9,#8f6449)" role="img" aria-label="Community member portrait"></div>
  <div class="abs photo" style="left:625px;top:902px;width:67px;height:64px;background:linear-gradient(135deg,#dedede,#a97e62)" role="img" aria-label="Community member portrait"></div>
  <div class="abs join-btn">JOIN TO US</div>
</section>

<footer>
  <div class="abs footer"></div>
  <div class="abs f-head" style="left:88px">Quick Links</div>
  <div class="abs f-link" style="left:90px;top:1100px">Plans<br>Benefits<br>FAQs<br>About Us</div>
  <div class="abs f-link" style="left:197px;top:1100px">Support<br>Privacy Policy<br>Terms &amp; Conditions<br>Contact Us</div>
  <div class="abs f-head" style="left:310px">E- Newsletter</div>
  <div class="abs field" style="top:1097px">Enter the first name</div>
  <div class="abs field" style="top:1131px">Email Id</div>
  <div class="abs subscribe">SUBSCRIBE</div>
  <div class="abs f-head" style="left:530px">Follow Us</div>
  <div class="abs social" style="left:529px"></div>
  <div class="abs social" style="left:562px"></div>
  <div class="abs social" style="left:596px"></div>
  <div class="abs copy">© 2014.bramblequill.example</div>
</footer>
</body>
</html>
```